Umbrian Friars Roast: a new roasting company in Italy by real monks.

We need a logo and label design for a new coffee roastery in Italy, near Florence. We are real monks that roast coffee with wood. Very high quality. We would like to receive proposal for the logo "Umbrian Friars roast" design and labels. In the logo design a monk in black must be present but it must not be something serious or sad. The logo must have the writing "Umbrian Friars roast" more important and less important "Cloister of Stillwater". We like something similar to the attached logo but the monk can also be seen in the face and more smiling. Italianness could be expressed on the labels but not banal (see Tuscan mountains). About the label: Our customers must first buy the beauty of the package and labels and then taste the coffee. It could be something particular like the attachment that we really like or something modern. The important thing is that the labels must be beautiful, even colorful but sober and elegant. Attached you will find the text on the front and back of the label. You can visit our web site www.chiostrodellaquiete.it but the coffee is at the beginning, please visit our facebook https://www.facebook.com/www.prioratodivalleombrosa.org
IMPORTANT: We will not design the whole package but only a label on a neutral black package as attacched. What is important now is not the size of the package but the idea.
Now we just need an idea. The winner will be invited to a 1:1 job to perfect the labels of the 7 blends.

Target Market(s)

Retail

Industry/Entity Type

coffee

Requirements
Must have
• Monk design
Nice to have
• Something of special

```html
<!DOCTYPE html>
<html lang="en">
<head>
<meta charset="utf-8">
<title>Umbrian Friars Roast – The Aurora Blend labels</title>
<link rel="stylesheet" href="https://fonts.googleapis.com/css2?family=Oswald:wght@400;500;600&family=Roboto+Condensed:wght@400;700&display=swap">
<style>
  :root{
    --bg:#ffffff;
    --green:#1e4a42;
    --green-soft:#285a50;
    --orange:#ec6a4e;
    --cream:#f4ead6;
    --ink:#1d2a27;
    --paper:#ffffff;
    --mint:#5fc58f;
  }
  *{box-sizing:border-box;margin:0;padding:0}
  html,body{width:1200px;height:720px;overflow:hidden;background:var(--bg)}
  body{position:relative;font-family:"Roboto Condensed",sans-serif;color:var(--ink)}

  /* brand mark */
  .brand{position:absolute;left:0;right:0;top:40px;display:flex;justify-content:center;align-items:center;gap:16px}
  .brand-dot{width:30px;height:30px;border-radius:50%;background:var(--orange)}
  .brand-name{font-family:"Oswald",sans-serif;font-weight:600;font-size:44px;letter-spacing:3px;color:var(--green);text-transform:uppercase}

  /* shared label parts */
  .label{position:absolute;background:var(--green)}
  .mini-brand{display:flex;align-items:center;justify-content:center;gap:6px}
  .mini-brand .dot{width:10px;height:10px;border-radius:50%;background:var(--paper)}
  .mini-brand .name{font-family:"Oswald",sans-serif;font-weight:600;font-size:13px;letter-spacing:1px;color:var(--paper);text-transform:uppercase}

  /* front label */
  .front{left:120px;top:200px;width:440px;height:440px}
  .front-panel{position:absolute;left:14px;right:14px;top:16px;height:330px;background:var(--orange)}
  .front .mini-brand{position:absolute;top:16px;left:0;right:0}
  .front-title{position:absolute;top:46px;left:0;right:0;text-align:center;font-family:"Oswald",sans-serif;font-weight:500;font-size:42px;color:var(--cream);text-transform:uppercase}
  .claim{position:absolute;left:10px;top:160px;width:80px;font-family:"Oswald",sans-serif;font-weight:500;font-size:21px;line-height:1.02;color:var(--green);text-transform:uppercase}
  .spec{position:absolute;left:94px;top:122px;width:308px;height:170px;background:var(--paper);border:2px solid var(--green);display:flex}
  .spec-side{width:26px;border-right:1.5px solid var(--green);display:flex;align-items:center;justify-content:center}
  .spec-side span{writing-mode:vertical-rl;transform:rotate(180deg);font-family:"Oswald",sans-serif;font-weight:600;font-size:20px;color:var(--green);letter-spacing:1px}
  .spec-body{flex:1;padding:6px 8px;display:flex;flex-direction:column}
  .spec-text{font-size:9.5px;line-height:1.25}
  .spec-table{display:flex;margin-top:8px;border-top:1px solid var(--ink)}
  .spec-table div{padding:3px 6px;font-size:9px;border-right:1px solid var(--ink)}
  .spec-table div:last-child{border-right:none}
  .spec-table b{display:block;font-size:9.5px}
  .roast{display:flex;align-items:center;gap:4px;margin-top:8px;font-size:7px;text-transform:uppercase}
  .roast-bar{flex:1;height:10px;border:1px solid var(--ink);background:linear-gradient(90deg,var(--orange) 0 42%,var(--paper) 42%)}
  .spec-strip{margin-top:auto;border:1.5px solid var(--green);text-align:center;font-size:10.5px;font-weight:700;letter-spacing:.5px;padding:4px 0;color:var(--green)}
  .front-foot{position:absolute;left:0;right:0;bottom:14px;text-align:center;font-size:9.5px;line-height:1.25;color:var(--cream);text-transform:uppercase}
  .pill{display:inline-block;margin-top:6px;padding:3px 18px;border-radius:10px;background:var(--mint);color:var(--paper);font-size:9px;letter-spacing:.5px}
  .roast-badge{position:absolute;left:26px;bottom:30px;width:22px;height:22px;border-radius:50%;background:var(--orange)}
  .weight{position:absolute;right:26px;bottom:34px;font-family:"Oswald",sans-serif;font-weight:500;font-size:18px;color:var(--cream)}

  /* back label */
  .back{right:120px;top:190px;width:400px;height:470px}
  .back-panel{position:absolute;inset:16px;background:var(--orange);color:var(--paper);padding:16px 18px}
  .back-head{display:flex;align-items:center;justify-content:center;gap:12px}
  .back-head .mini-brand .dot{background:var(--green)}
  .back-head .mini-brand .name{color:var(--green)}
  .back-title{font-family:"Oswald",sans-serif;font-weight:500;font-size:26px;line-height:.95;color:var(--cream);text-transform:uppercase}
  .back-lead{margin-top:12px;text-align:center;font-size:11px;line-height:1.25}
  .back-copy{margin-top:8px;text-align:center;font-size:7.6px;line-height:1.3}
  .back-copy p+p{margin-top:6px}
  .back-foot{position:absolute;left:18px;right:18px;bottom:14px;display:flex;align-items:flex-end;gap:10px}
  .producer{flex:1;text-align:center;font-size:7.4px;line-height:1.3}
  .best{width:96px;background:var(--paper);color:var(--ink);font-size:7px}
  .best-head{background:var(--green);color:var(--paper);font-weight:700;padding:2px 4px;text-transform:uppercase}
  .best-body{height:44px;padding:2px 4px}
  .nature-badge{width:30px;height:30px;border-radius:50%;background:var(--paper)}
</style>
</head>
<body>

  <header class="brand">
    <span class="brand-dot"></span>
    <span class="brand-name">Umbrian Friars Roast</span>
  </header>

  <section class="label front" aria-label="Front label">
    <div class="front-panel">
      <div class="mini-brand"><span class="dot"></span><span class="name">Umbrian Friars Roast</span></div>
      <h1 class="front-title">The Aurora Blend</h1>
      <p class="claim">100% Wood Roasted Coffee</p>
      <div class="spec">
        <div class="spec-side"><span>ARABICA</span></div>
        <div class="spec-body">
          <p class="spec-text">Indulge in our 100% Arabica coffee blend, featuring sweet, exotic fruit and spice notes, medium-strong intensity, and lively citrus and floral hints of orange and bergamot.</p>
          <div class="spec-table">
            <div>PROCESS:<b>WOOD ROASTED</b></div>
            <div>REGION<b>TUSCANY</b></div>
            <div>REGION<b>HIGH</b></div>
          </div>
          <div class="roast"><span>Light</span><span class="roast-bar"></span><span>Dark</span></div>
          <p class="spec-strip">ROASTED TO ORDER, JUST BEFORE SHIPPING</p>
        </div>
      </div>
    </div>
    <span class="roast-badge" role="img" aria-label="Wood-fire roast badge"></span>
    <div class="front-foot">
      Italian high quality coffee<br>Roasted by the friars of the Cloister<br>of Stillwater in Tuscany<br>
      <span class="pill">WWW.UMBRIANFRIARS.COFFEE</span>
    </div>
    <span class="weight">250 GR</span>
  </section>

  <section class="label back" aria-label="Back label">
    <div class="back-panel">
      <div class="back-head">
        <div class="mini-brand"><span class="dot"></span><span class="name">Umbrian Friars Roast</span></div>
        <h2 class="back-title">The Aurora<br>Blend</h2>
      </div>
      <p class="back-lead">Umbrian Friars Roast blended and wood roasted in the mountains near Florence by the Cloister of Stillwater Friars</p>
      <div class="back-copy">
        <p>In their monastery nestled deep in the Mugello mountains the friars blend and roast their coffee.</p>
        <p>The quiet meadows echo no sound but the occasional movements of a deer or a wild boar in the black pine forests. The delightful song of a meadow lark welcomes the rising sun that lights up the mountain lake where a lonely ancient monastery sits. The mountain peaks begin to twinkle orange in the bright morning sun. A gentle breeze plays with a peaceful cloud of what appears to be a typical mountain fog across the field before the monastery. But it is not a fog. It is the delicious smoke of this morning's dark coffee roast.</p>
        <p>Every morning after prayers, a few of the friars walk down to their roasting barn whose yellow walls glimmer in the sunrise. They are ready to roast the coffee for today's blessed recipients. Curious about how our friars achieve their coffee mastery at 850 meters altitude in the picturesque Mugello mountains near Florence? Rest assured, our master roaster, with over 40 years of expertise, evokes the rich coffee traditions cherished by connoisseurs for fifteen years and beyond.</p>
      </div>
      <div class="back-foot">
        <p class="producer">Italian blend of roasted coffee beans<br>Produced and packaged by <b>the Cloister of Stillwater – Priorato di Valleombrosa – Tuscany</b><br>REA 0481937265<br>www.umbrianfriars.coffee<br>www.stillwatercloister.it<br>Net Weight 250 gr e 35,2 oz</p>
        <div class="best"><div class="best-head">Keep in a cool and dry place</div><div class="best-body">Best before</div></div>
        <span class="nature-badge" role="img" aria-label="Environmental badge"></span>
      </div>
    </div>
  </section>

</body>
</html>
```